Texas Civic Builders Summit Needs a Flyer

One-page event graphic/flyer and header needed. Logos provided.

2023 Texas Civic Builders Summit
Bold Ventures – True Accounts, True Answers, True Wins
August 10-11, 2023
San Antonio, Texas

About the Forum:
“Capital projects are full of risk. It’s not a question of eliminating risk, it’s a question of how to clearly identify it, reduce it, change it, or battle it.”
- Denise Holmgarten, Founder, U-BraMQ; San Antonio City Architect (retired)

Real Stories, Real Solutions, Real Success: U-BraMQ’s Texas Civic Builders Summit (TCBS) is designed to help you attain project success by hearing from Public Project Owners, architects, engineers, consultants, contractors, and suppliers. We are all in this together, and U-BraMQ is the organization that champions cross-collaboration and communication for project success!

For reference in design ONLY -
Here are some topic areas that bring project risks and/or rewards and that ultimately affect the Public Project Owner’s project success:

• Project Planning
• Regional Growth Shifts
• Project Funding
• Contracting
• Governmental Regulations
• Long-term COVID Impacts
• Infrastructure and Site Design
• Safety and Security
• Sustainability and Resilience
• Construction Predictability
• Leveraging Technology
• Facility Operations

Target Market(s)

Architects, Engineers, Contractors, project owners

Industry/Entity Type

Design and Construction

Requirements
Must have
• This is for a one-page (8.5x11) event graphic/flyer only - logos are provided. U-BraMQ logo, Texas Civic Builders Summit (TCBS) logo, 2023 Texas Civic Builders Summit, date, location
Nice to have
• Graphic(s) that represent the design and construction industry and the theme of this event (title, topics covered)
Should not have
• Full project description

```html
<!DOCTYPE html>
<html lang="en">
<head>
<meta charset="utf-8">
<title>2023 Texas Civic Builders Summit – Flyer</title>
<link rel="stylesheet" href="https://fonts.googleapis.com/css2?family=Oswald:wght@500;600&family=Ubuntu:ital,wght@0,400;0,500;1,400&display=swap">
<style>
  :root {
    --page-bg: #3b3a39;
    --brand-blue: #2c4aa3;
    --sky-blue: #3556b8;
    --accent-green: #8cc63f;
    --text-blue: #22397f;
    --white: #ffffff;
    --haze: #dfe6f3;
  }
  * { margin: 0; padding: 0; box-sizing: border-box; }
  html, body { width: 1200px; height: 800px; overflow: hidden; }
  body { background: var(--page-bg); position: relative; font-family: "Ubuntu", sans-serif; }

  .flyer {
    position: absolute; left: 306px; top: 20px;
    width: 612px; height: 792px;
    transform: scale(0.96); transform-origin: top left;
    background: linear-gradient(180deg, #ffffff 0%, var(--haze) 60%, #c9d5ec 100%);
    overflow: hidden;
  }

  .header {
    position: absolute; left: 0; top: 0; width: 612px; height: 188px;
    background: linear-gradient(180deg, var(--sky-blue), var(--brand-blue));
    text-align: center;
  }
  .event-label {
    margin-top: 18px;
    font-weight: 500; font-size: 18px; letter-spacing: -0.2px;
    color: var(--accent-green);
  }
  .title {
    margin-top: 6px;
    font-family: "Oswald", sans-serif; font-weight: 600;
    font-size: 46px; line-height: 52px; color: var(--white);
  }
  .subtitle {
    font-family: "Oswald", sans-serif; font-weight: 500;
    font-size: 31px; line-height: 38px; color: var(--white);
    letter-spacing: -0.3px;
  }
  .date-pill {
    position: absolute; left: 116px; top: 165px;
    width: 380px; height: 40px; border-radius: 20px;
    background: var(--accent-green); border: 2px solid var(--white);
    font-family: "Oswald", sans-serif; font-weight: 500;
    font-size: 23px; line-height: 36px; color: var(--white); text-align: center;
    z-index: 2;
  }

  .city-haze {
    position: absolute; left: 180px; top: 300px; width: 432px; height: 320px;
    background: linear-gradient(180deg, rgba(184,199,228,0) 0%, rgba(184,199,228,0.55) 55%, rgba(200,212,236,0.2) 100%);
  }

  .intro {
    position: absolute; left: 27px; top: 224px; width: 345px;
    font-size: 12.6px; line-height: 17.5px; color: var(--text-blue);
  }
  .topics { position: absolute; left: 26px; top: 301px; list-style: none; }
  .topics li {
    font-size: 13.4px; line-height: 20px; color: var(--text-blue); font-weight: 500;
    padding-left: 17px; position: relative;
  }
  .topics li::before {
    content: ""; position: absolute; left: 0; top: 5px;
    width: 9px; height: 9px; border-radius: 50%;
    border: 1.5px solid var(--accent-green); background: var(--white);
    box-shadow: inset 0 0 0 1.5px var(--white), inset 0 0 0 4px var(--brand-blue);
  }

  .quote-mark { position: absolute; left: 30px; top: 552px; }
  .quote {
    position: absolute; left: 28px; top: 556px; width: 280px;
    font-size: 9.3px; line-height: 13px; font-style: italic; color: var(--text-blue);
    letter-spacing: -0.3px;
  }
  .quote p { text-indent: 30px; }

  .skyline {
    position: absolute; left: 0; top: 615px; width: 612px; height: 105px;
    background: linear-gradient(180deg, rgba(44,74,163,0) 0%, rgba(44,74,163,0.85) 45%, var(--brand-blue) 100%);
  }
  .footer {
    position: absolute; left: 0; top: 716px; width: 612px; height: 76px;
    background: var(--brand-blue);
  }
  .org-name {
    position: absolute; display: flex; align-items: center; gap: 8px;
    color: var(--white); font-weight: 500;
  }
  .org-primary { left: 30px; top: 16px; font-size: 24px; }
  .org-primary .mark { width: 40px; height: 40px; border-radius: 50%; background: var(--white); }
  .org-secondary { left: 222px; top: 20px; font-size: 13px; line-height: 15px; width: 120px; }

  .worker-photo {
    position: absolute; left: 350px; top: 213px; width: 262px; height: 579px;
    background: linear-gradient(180deg, rgba(230,226,220,0.35) 0%, rgba(196,140,120,0.55) 40%, rgba(200,160,90,0.6) 80%, rgba(90,80,80,0.6) 100%);
  }
</style>
</head>
<body>
  <article class="flyer">
    <header class="header">
      <p class="event-label">2023 TEXAS CIVIC BUILDERS SUMMIT</p>
      <h1 class="title">BOLD VENTURES</h1>
      <p class="subtitle">TRUE ACCOUNTS, TRUE ANSWERS, TRUE WINS</p>
    </header>
    <p class="date-pill">AUGUST 10-11, SAN ANTONIO, TEXAS</p>

    <div class="city-haze" role="img" aria-label="Faint city skyline photograph in the background"></div>

    <p class="intro">With a limited attendance, THIS IS YOUR OPPORTUNITY to experience an intimate, safe environment where project pains and triumphs, challenges and solutions, risks and rewards, are shared openly.</p>

    <ul class="topics">
      <li>Project Planning</li>
      <li>Regional Growth Shifts</li>
      <li>Project Funding</li>
      <li>Contracting</li>
      <li>Governmental Regulations</li>
      <li>Long-term COVID Impacts</li>
      <li>Infrastructure and Site Design</li>
      <li>Safety and Security</li>
      <li>Sustainability and Resilience</li>
      <li>Construction Predictability</li>
      <li>Leveraging Technology</li>
      <li>Facility Operations</li>
    </ul>

    <svg class="quote-mark" width="26" height="20" viewBox="0 0 26 20" aria-hidden="true">
      <path d="M2 20 V10 Q2 2 10 0 L11 3 Q6 5 6 10 H10 V20 Z M15 20 V10 Q15 2 23 0 L24 3 Q19 5 19 10 H23 V20 Z" fill="#8cc63f"/>
    </svg>
    <blockquote class="quote">
      <p>Capital projects are full of risk. It’s not a question of eliminating risk, it’s a question of how to clearly identify it, reduce it, change it, or battle it.” - Denise Holmgarten, Founder, U-BraMQ; San Antonio City Architect (retired)</p>
    </blockquote>

    <div class="skyline" role="img" aria-label="Blue city skyline silhouette"></div>
    <footer class="footer">
      <div class="org-name org-primary"><span class="mark"></span>U-BraMQ</div>
      <div class="org-name org-secondary">Texas Civic Builders Conference</div>
    </footer>

    <div class="worker-photo" role="img" aria-label="Photograph of a construction worker in a hard hat, plaid shirt and tool belt"></div>
  </article>
</body>
</html>
```